Business Card Design For Office Furniture Clearance Company

Kestrel Office Clearance - our company name pretty much explains what we do, we clear offices for high end clients, mainly plc's and large international companies.

We require a nice looking business card that displays professionalism but without being too serious.

It would be nice to see just a little more than a conventional boring business card, make sure you add some flare.

Industry/Entity Type

Office Furniture

Contact Information for Business Card

CARD 1

Tom Pardew
Director
tom@kestrelofficeclearance.co.uk
m: 07700 513928

t: 01632 419063
www.kestrelofficeclearance.co.uk

Kestrel Office Clearance
Unit K4 B
3-7 Ferndale Lane
Ashcombe
Harrowfield
ZZ9 4QX

clear desks, clear floors… all at no cost to you.

CARD 2

Henry Walbrook
Director
henry@kestrelofficeclearance.co.uk
m: 07700 628157

t: 01632 419063

Kestrel Office Clearance
Unit K4 B
3-7 Ferndale Lane
Ashcombe
Harrowfield
ZZ9 4QX

Font styles to use
Sans Serif

Requirements
Must have
• A white background - as we have a blue logo.
Nice to have
• Nice use of the logo - play around with this and dissect it.

```html
<!DOCTYPE html>
<html lang="en">
<head>
<meta charset="utf-8">
<title>Kestrel Office Clearance – Business Card</title>
<link rel="stylesheet" href="https://fonts.googleapis.com/css2?family=Open+Sans:ital,wght@0,400;0,600;0,700;1,400&display=swap">
<style>
  :root {
    --brand-blue: #1577bd;
    --brand-blue-deep: #0b5a98;
    --brand-blue-soft: #2d8ad0;
    --card-white: #ffffff;
    --ink-grey: #5c6670;
    --stage: #e9ebee;
    --font-main: "Open Sans", Arial, sans-serif;
  }
  * { box-sizing: border-box; margin: 0; padding: 0; }
  html, body { width: 1200px; height: 950px; overflow: hidden; }
  body { background: var(--stage); font-family: var(--font-main); position: relative; }

  .card {
    position: absolute;
    width: 620px;
    height: 400px;
    border-radius: 6px;
    overflow: hidden;
    box-shadow: 0 10px 30px rgba(0,0,0,0.18);
  }

  /* Front */
  .card-front {
    left: 80px; top: 80px;
    background: linear-gradient(160deg, var(--brand-blue-soft) 0%, var(--brand-blue) 45%, var(--brand-blue-deep) 100%);
    color: var(--card-white);
  }
  .front-disc {
    position: absolute;
    right: -90px; top: -120px;
    width: 420px; height: 420px;
    border-radius: 50%;
    background: rgba(255,255,255,0.14);
  }
  .front-wordmark {
    position: absolute;
    right: 40px; top: 70px;
    font-size: 88px;
    font-weight: 700;
    letter-spacing: -2px;
    color: var(--card-white);
  }
  .contact {
    position: absolute;
    left: 44px; bottom: 36px;
    font-size: 14px;
    line-height: 1.45;
  }
  .contact-name {
    font-size: 22px;
    font-weight: 600;
    text-transform: uppercase;
    letter-spacing: 0.5px;
    line-height: 1.1;
  }
  .contact-role {
    font-size: 12px;
    text-transform: uppercase;
    letter-spacing: 1px;
    margin-bottom: 14px;
  }
  .contact-company { font-weight: 700; }
  .contact-address { margin-bottom: 12px; }
  .contact-line { display: flex; align-items: center; gap: 8px; }
  .contact-line svg { width: 13px; height: 13px; flex: none; }

  /* Back */
  .card-back {
    left: 500px; top: 470px;
    background: var(--card-white);
  }
  .back-mark {
    position: absolute;
    left: 50%; top: 70px;
    transform: translateX(-50%);
    display: flex;
    flex-direction: column;
    align-items: center;
    gap: 18px;
  }
  .back-disc {
    width: 170px; height: 170px;
    border-radius: 50%;
    background: var(--brand-blue);
  }
  .back-wordmark {
    font-size: 22px;
    font-weight: 700;
    color: var(--brand-blue);
    white-space: nowrap;
  }
  .tagline {
    position: absolute;
    left: 40px; bottom: 34px;
    font-size: 15px;
    font-style: italic;
    color: var(--ink-grey);
  }
</style>
</head>
<body>

<section class="card card-front" aria-label="Business card front">
  <div class="front-disc"></div>
  <div class="front-wordmark">Kestrel</div>

  <div class="contact">
    <p class="contact-name">Tom Pardew</p>
    <p class="contact-role">Director</p>
    <p class="contact-company">Kestrel Office Clearance</p>
    <p class="contact-address">Unit K4 B, 3-7 Ferndale Lane<br>Ashcombe, Harrowfield<br>ZZ9 4QX</p>

    <p class="contact-line">
      <svg viewBox="0 0 16 16" aria-hidden="true"><path fill="currentColor" d="M3.5 1.5l2.5 0 1 3.5-1.8 1.2a8 8 0 0 0 4.6 4.6L11 9l3.5 1v2.5c0 1-1 2-2 2A11 11 0 0 1 1.5 3.5c0-1 1-2 2-2z"/></svg>
      01632 419063
    </p>
    <p class="contact-line">
      <svg viewBox="0 0 16 16" aria-hidden="true"><rect x="4" y="1" width="8" height="14" rx="1.5" fill="none" stroke="currentColor" stroke-width="1.6"/><circle cx="8" cy="12.5" r="0.9" fill="currentColor"/></svg>
      07700 513928
    </p>
    <p class="contact-line">
      <svg viewBox="0 0 16 16" aria-hidden="true"><rect x="1" y="3" width="14" height="10" rx="1" fill="currentColor"/><path d="M1.5 3.5L8 9l6.5-5.5" fill="none" stroke="#1577bd" stroke-width="1.4"/></svg>
      tom@kestrelofficeclearance.co.uk
    </p>
    <p class="contact-line">
      <svg viewBox="0 0 16 16" aria-hidden="true"><circle cx="8" cy="8" r="6.5" fill="none" stroke="currentColor" stroke-width="1.4"/><ellipse cx="8" cy="8" rx="2.8" ry="6.5" fill="none" stroke="currentColor" stroke-width="1.2"/><path d="M1.5 8h13" stroke="currentColor" stroke-width="1.2"/></svg>
      www.kestrelofficeclearance.co.uk
    </p>
  </div>
</section>

<section class="card card-back" aria-label="Business card back">
  <div class="back-mark">
    <div class="back-disc"></div>
    <p class="back-wordmark">Kestrel Office Clearance</p>
  </div>
  <p class="tagline">clear desks, clear floors… all at no cost to you.</p>
</section>

</body>
</html>
```